Coastal Rubdown Oil Co. needs a new label.

This massage oil has been in Australia for over 20 years and needs a new label for its plastic 250ml bottles. The current label (8cm x 8cm) looks old fashioned and so we are looking for something that reflects freedom, relaxation, inspiration. The product is made from sweet almond oil and has different essential oils used to give unique smells. I have seen some lovely abstract vector images. I think we need a clean straight look with bright colours. There are currently six variations to the product. "Weary and Worn Heads, Achy and Spent Frames, Couples Mix, Heather Soak Oil, Unwinding Mix, Uplift Mix" Different coloured labels have been used for each of the blends. I have included photos of existing bottles plus some ideas for the labels.

I would like to use the same font on the name of the brand Bramblewick Acres. If we change the font it may be difficult for existing customers to find our product.

Also just under the name Bramblewick Acres I would like to insert a type of logo (can be the shape of a tear drop or round circle) to say:

Massage Oil
Since 1970

The size of the label is 8cm x 12 cm for the front and the same size for the back of the label.
Updates

Coastal Rubdown oil Company has posted on the brief some images from Pixelvault plus two photos of the original bottles. I am looking for a new design which is bright in colour, fun and funky. I am not thinking along the lines of the traditional Herb and trees look. I think the original label is too busy and the colours overpower the label. The other point I think that is important is that the product has been around since 1970. If there is room I think a round logo which says: Massage Oil Since 1970 I am hoping that we can fit this information on the label Looking forward to seeing all the designs come thru. So far I have only had two designs come thru. Speak soon from hot sunny Australia. maree

Thank you to everyone who has already posted designs for our Massage Label. I have now edited the brief to include some more ideas on how to make this design the Best! I will email back to you straight away ideas and thoughts on your designs. Remember I live in Australia and can be either 10hrs in front or behind your time.

Reason: Due to busy lives and commitments over the next few days I feel that an extension will benefit all involved. Thank you to everyone who has submitted designs and working with me to create something beautiful. maree

Hello from Australia all the designers who have submitted some wonderful designs over the past two weeks. We are now entering the final three days of the competition. Thank you to everyone who has worked so hard to try and create the perfect label for my massage oil bottle. All of you have done a fantastic job. This has made the decision hard to make. Thank you to everyone. Please submit all your last minute designs soon. kind regards maree Australia

Target Market(s)

The type of person purchasing a massage oil blend will buy from a health food shop, pharmacy or from an on-line store. I believe they are wanting something bright that clearly communicates that that it is a massage oil.

Industry/Entity Type

Massage

Font styles to use
Script

Requirements
Must have
• Different colour for each massage oil blend.
Need same font for the name Bramblewick Acres. (script font or similar)

Abstract design please.
Nice to have
• A logo under the name Bramblewick Acres

Tear Drop or circle design that says:

Massage Oil
Since 1970

also we would like an outline for the back label. (see photo attached)

BACK LABEL information

A unique blend of essential oils in a fine light base.

Contains:

vegetable oil extract of nettle, sweet almond oil, ethanol, essential oils of lavender, lemongrass, orange & ylang ylang and vitamin E.

How to Use:

Shake well warm bottle in warm water if very cold.
Lovingly massage the body from head to toe.
Not for medicinal use.

Bramblewick Acres
Hollin WA 6099
Phone: (08) 9555 0142

(LEAVE ROOM FOR BARCODE)
Should not have
• Too busy design or old fashioned design.
No dull colours.

```html
<!DOCTYPE html>
<html lang="en">
<head>
<meta charset="utf-8">
<title>Bramblewick Acres – Heather Soak Oil Label</title>
<link rel="stylesheet" href="https://fonts.googleapis.com/css2?family=Great+Vibes&family=Cinzel:wght@400;600&family=Crimson+Text:wght@400;600&family=Roboto+Condensed:wght@400;700&display=swap">
<style>
  :root {
    --page: #ffffff;
    --label: #c8b4d9;
    --purple: #5a2486;
    --purple-deep: #4a1a72;
    --ink: #4b1d78;
    --white: #ffffff;
    --art-light: #ddd0e8;
    --art-mid: #a582c4;
    --art-green: #cfe0b6;
  }
  * { margin: 0; padding: 0; box-sizing: border-box; }
  html, body { width: 1200px; height: 900px; overflow: hidden; background: var(--page); }
  .canvas { position: relative; width: 1200px; height: 900px; }

  .label {
    position: absolute;
    top: 76px;
    width: 480px;
    height: 720px;
    background: var(--label);
    overflow: hidden;
  }
  .label--front { left: 110px; }
  .label--back { left: 624px; }

  /* Front */
  .brand-name {
    position: absolute; top: 130px; left: 0; width: 100%;
    text-align: center;
    font-family: "Great Vibes", cursive;
    font-size: 64px; line-height: 1;
    color: var(--purple);
  }
  .brand-mark {
    position: absolute; top: 207px; left: 231px;
    width: 18px; height: 18px; border-radius: 50%;
    background: var(--purple);
  }
  .product-type {
    position: absolute; top: 234px; left: 0; width: 100%;
    text-align: center;
    font-family: "Cinzel", serif; font-weight: 600;
    font-size: 30px; color: var(--purple);
  }
  .since {
    position: absolute; top: 274px; left: 0; width: 100%;
    text-align: center;
    font-family: "Cinzel", serif; font-weight: 600;
    font-size: 16px; color: var(--purple);
  }
  .floral-art--front {
    position: absolute; top: 210px; left: 0; width: 480px; height: 460px;
    top: 214px;
    background:
      radial-gradient(circle at 20% 30%, var(--art-mid) 0 60px, transparent 62px),
      radial-gradient(circle at 78% 22%, var(--white) 0 70px, transparent 72px),
      radial-gradient(circle at 18% 80%, var(--white) 0 70px, transparent 72px),
      radial-gradient(circle at 85% 75%, var(--art-mid) 0 66px, transparent 68px),
      radial-gradient(ellipse at 50% 55%, var(--art-light), transparent 70%);
    opacity: .85;
  }
  .floral-art--front { top: 214px; height: 450px; }

  .title-banner {
    position: absolute;
    display: flex; align-items: center; justify-content: center;
    background: var(--purple);
    border: 3px solid var(--purple-deep);
    box-shadow: inset 0 0 0 2px var(--white), inset 0 0 0 5px var(--purple);
    border-radius: 14px;
    font-family: "Cinzel", serif;
    color: var(--white);
    white-space: nowrap;
  }
  .title-banner--front {
    left: 74px; top: 526px; width: 332px; height: 76px;
    font-size: 31px;
  }
  .banner-rule {
    position: absolute; left: 50%; transform: translateX(-50%);
    height: 2px; background: var(--white); opacity: .8;
  }
  .title-banner--front .banner-rule { top: 9px; width: 70px; }
  .volume {
    position: absolute; top: 648px; left: 0; width: 100%;
    text-align: center;
    font-family: "Crimson Text", serif; font-size: 22px;
    color: var(--ink);
  }

  /* Back */
  .floral-art--side {
    position: absolute; top: 140px; width: 120px; height: 360px;
    background: linear-gradient(180deg, var(--white) 0%, var(--art-mid) 35%, var(--art-green) 55%, var(--art-mid) 80%, var(--art-light) 100%);
    opacity: .7;
    border-radius: 60px;
  }
  .floral-art--left { left: -40px; }
  .floral-art--right { right: -40px; }

  .info-panel {
    position: absolute; left: 100px; top: 140px; width: 276px; height: 444px;
    border: 2px solid var(--white);
    border-radius: 32px;
    background: var(--label);
  }
  .title-banner--back {
    left: 116px; top: 104px; width: 244px; height: 68px;
    font-size: 21px; font-weight: 600;
  }
  .title-banner--back .banner-rule { top: 9px; width: 54px; }
  .info-text {
    position: absolute; left: 104px; top: 200px; width: 268px;
    text-align: center;
    font-family: "Crimson Text", serif;
    font-size: 15.5px; line-height: 1.22;
    color: var(--ink);
  }
  .info-text p { margin-bottom: 16px; }
  .info-text .info-head { margin-bottom: 0; }
  .info-text .spacer { height: 20px; }

  .maker {
    position: absolute; left: 148px; top: 612px;
    font-family: "Roboto Condensed", sans-serif;
    color: var(--ink);
    font-size: 13px; line-height: 1.5;
  }
  .maker-dot {
    position: absolute; left: -22px; top: 4px;
    width: 14px; height: 14px; border-radius: 50%;
    background: var(--purple);
  }
  .maker-name { font-weight: 700; }
</style>
</head>
<body>
<main class="canvas">

  <section class="label label--front" aria-label="Front label">
    <div class="floral-art floral-art--front" role="img" aria-label="Illustrated bouquet of purple and white flowers with green leaves and swirling stems"></div>
    <h1 class="brand-name">Bramblewick Acres</h1>
    <span class="brand-mark"></span>
    <p class="product-type">MASSAGE OIL</p>
    <p class="since">SINCE 1970</p>
    <div class="title-banner title-banner--front"><span class="banner-rule"></span>Heather Soak Oil</div>
    <p class="volume">250 ml</p>
  </section>

  <section class="label label--back" aria-label="Back label">
    <div class="floral-art floral-art--side floral-art--left" role="img" aria-label="Partial floral illustration of white and purple blooms with leaves"></div>
    <div class="floral-art floral-art--side floral-art--right" role="img" aria-label="Partial floral illustration of purple blooms with leaves and stems"></div>
    <div class="info-panel"></div>
    <div class="title-banner title-banner--back"><span class="banner-rule"></span>Heather Soak Oil</div>
    <div class="info-text">
      <p>A unique blend of essential<br>oils in a fine light base.</p>
      <p class="info-head">CONTAINS:</p>
      <p>Vegetable oil extract of nettle, sweet almond oil, ethanol, essential oils of lavender, lemongrass, orange and yland-ylang and Vitamin E.</p>
      <div class="spacer"></div>
      <p class="info-head">HOW TO USE:</p>
      <p>Shake well. Warm bottle in warm water is very cold. Lovingly massage the body from head to toe. Not for medicinal use.</p>
    </div>
    <address class="maker" style="font-style:normal">
      <span class="maker-dot"></span>
      <div class="maker-name">BRAMBLEWICK ACRES</div>
      <div>Hollin, WA 6099</div>
      <div>Phone: (08) 9555 0142</div>
    </address>
  </section>

</main>
</body>
</html>
```